AWESOME CYBER MONDAY SALE AD NEEDED

Create a Cyber Monday ad for nitrile gloves. We are offering a box of 100, no-powder, exam grade nitrile gloves, for $9.99. No limit. Each case is $99. Create something simple, eye catching, cool. KelpTorch.com. Sale ends on December 4th. While supplies last. We are a local medical supply company in Hawaii that serves the general public in addition to local businesses, government, etc. Gloves are in short supply and we have tons of inventory ready to sell.

Target Market(s)

Businesses that use supplies such as gloves

Industry/Entity Type

medical supplies

Requirements
Must have
• The company logo, website, picture of gloves and pricing.

```html
<!DOCTYPE html>
<html lang="en">
<head>
<meta charset="utf-8">
<title>KelpTorch.com — Cyber Monday Nitrile Gloves Sale</title>
<link href="https://fonts.googleapis.com/css2?family=Montserrat:ital,wght@0,400;0,500;0,600;0,700;0,800;0,900;1,800;1,900&display=swap" rel="stylesheet">
<style>
  :root {
    --page: #ffffff;
    --royal: #3a02b0;
    --violet: #3d12c8;
    --offer-violet: #3a12c4;
    --magenta: #8a1c9c;
    --cyan: #12c8f0;
    --ink: #111111;
    --white: #ffffff;
    --sale-yellow: #ffee00;
    --brand-green: #2a8a2e;
  }
  * { box-sizing: border-box; margin: 0; padding: 0; }
  html, body { width: 1200px; height: 847px; overflow: hidden; background: var(--page); }
  body { position: relative; font-family: "Montserrat", sans-serif; color: var(--white); }

  .ad { position: absolute; overflow: hidden; }
  .ad--poster { left: 107px; top: 80px; width: 410px; height: 685px; background: var(--royal); }
  .ad--banner { left: 572px; top: 229px; width: 519px; height: 386px; background: var(--royal); }

  .glove-photo { position: absolute; left: 0; top: 0; width: 100%; }
  .ad--poster .glove-photo {
    height: 450px;
    background:
      radial-gradient(ellipse 140px 180px at 270px 150px, rgba(47,99,240,.95), transparent 70%),
      radial-gradient(ellipse 120px 90px at 80px 60px, rgba(220,214,248,.95), transparent 75%),
      radial-gradient(ellipse 160px 120px at 120px 320px, rgba(190,184,240,.8), transparent 70%),
      linear-gradient(180deg, #9b93e6 0%, #6f5fe0 55%, var(--royal) 100%);
  }
  .ad--banner .glove-photo {
    height: 100%;
    background:
      radial-gradient(ellipse 120px 150px at 450px 300px, rgba(47,99,240,.95), transparent 70%),
      radial-gradient(ellipse 60px 110px at 40px 250px, rgba(90,160,250,.9), transparent 75%),
      radial-gradient(ellipse 180px 120px at 180px 80px, rgba(215,208,246,.9), transparent 72%),
      radial-gradient(ellipse 200px 140px at 260px 300px, rgba(200,196,240,.7), transparent 70%),
      linear-gradient(90deg, #7d70e4 0%, #6a5ee0 60%, #2a0a90 92%, #1a0050 100%);
  }

  .brand-tag {
    position: absolute; background: var(--white);
    outline: 1px solid var(--white); outline-offset: 3px;
    display: flex; align-items: center; justify-content: center;
    font-weight: 700; color: var(--brand-green); white-space: nowrap;
    font-size: 12px;
  }
  .ad--poster .brand-tag { left: 155px; top: 36px; width: 96px; height: 55px; }
  .ad--banner .brand-tag { left: 399px; top: 24px; width: 96px; height: 54px; }

  .promo-stamp { position: absolute; transform: rotate(-8deg); transform-origin: center; }
  .ad--poster .promo-stamp { left: 20px; top: 150px; width: 390px; }
  .ad--banner .promo-stamp { left: 50px; top: 86px; width: 340px; }

  .stamp-band { display: block; white-space: nowrap; line-height: 1; }
  .stamp-kicker {
    font-weight: 800; font-style: italic; color: var(--ink);
    background: linear-gradient(90deg, transparent, var(--white) 12%, var(--white) 80%, transparent);
  }
  .stamp-kicker .light { font-weight: 400; font-style: normal; }
  .stamp-title {
    font-weight: 800; color: var(--white); letter-spacing: 0.5px;
    background: linear-gradient(90deg, transparent, var(--magenta) 8%, #5a16b8 45%, var(--violet) 85%, transparent);
  }
  .stamp-sale {
    font-weight: 900; font-style: italic; color: var(--violet);
    background: linear-gradient(90deg, transparent, var(--white) 15%, var(--white) 75%, transparent);
  }
  .ad--poster .stamp-kicker { font-size: 18px; padding: 6px 60px 6px 70px; margin-left: 40px; width: 300px; }
  .ad--poster .stamp-title { font-size: 41px; padding: 4px 10px 4px 14px; width: 400px; }
  .ad--poster .stamp-sale { font-size: 38px; padding: 0 70px 4px 120px; margin-left: 80px; width: 300px; }
  .ad--banner .stamp-kicker { font-size: 15px; padding: 5px 40px 5px 70px; margin-left: 40px; width: 250px; }
  .ad--banner .stamp-title { font-size: 34px; padding: 3px 10px 3px 14px; width: 350px; }
  .ad--banner .stamp-sale { font-size: 32px; padding: 0 50px 3px 110px; margin-left: 90px; width: 250px; }

  .product-title { position: absolute; overflow: visible; }
  .product-title text {
    font-family: "Montserrat", sans-serif; font-weight: 900;
    fill: url(#title-fill); stroke: var(--cyan); paint-order: stroke;
  }
  .ad--poster .product-title { left: 0; top: 296px; width: 410px; height: 150px; }
  .ad--banner .product-title { left: 0; top: 196px; width: 519px; height: 50px; }

  .offer-copy { position: absolute; text-align: center; line-height: 1.12; }
  .ad--poster .offer-copy { left: 0; top: 449px; width: 410px; font-size: 19px; font-weight: 500; }
  .ad--banner .offer-copy {
    left: 60px; top: 246px; width: 400px; font-size: 13.5px; font-weight: 700;
    color: var(--offer-violet); line-height: 1.3; white-space: nowrap;
    text-shadow:
      1px 0 0 var(--white), -1px 0 0 var(--white),
      0 1px 0 var(--white), 0 -1px 0 var(--white),
      1px 1px 0 var(--white), -1px -1px 0 var(--white),
      1px -1px 0 var(--white), -1px 1px 0 var(--white);
  }

  .sale-deadline {
    position: absolute; background: var(--sale-yellow); color: var(--ink);
    font-size: 11.5px; font-weight: 400; text-align: center; line-height: 20px;
    white-space: nowrap; width: 242px; height: 20px;
  }
  .ad--poster .sale-deadline { left: 75px; top: 523px; }
  .ad--banner .sale-deadline { left: 127px; top: 299px; }

  .case-price { position: absolute; display: flex; align-items: center; line-height: .86; }
  .case-label { font-weight: 500; text-transform: uppercase; }
  .case-amount { font-weight: 700; }
  .ad--poster .case-price { left: 100px; top: 566px; gap: 8px; }
  .ad--poster .case-label { font-size: 30px; letter-spacing: -0.5px; }
  .ad--poster .case-label .sm { font-size: 26px; display: block; }
  .ad--poster .case-amount { font-size: 58px; }
  .ad--banner .case-price { left: 387px; top: 296px; flex-direction: column; align-items: flex-start; }
  .ad--banner .case-label { font-size: 17px; }
  .ad--banner .case-label .sm { font-size: 13px; display: block; }
  .ad--banner .case-amount { font-size: 26px; margin-top: 2px; }

  .site-url { position: absolute; font-weight: 400; text-align: center; white-space: nowrap; }
  .ad--poster .site-url { left: 0; top: 632px; width: 410px; font-size: 20px; letter-spacing: 0.3px; }
  .ad--banner .site-url { left: 151px; top: 342px; width: 190px; font-size: 16px; color: var(--ink); }
</style>
</head>
<body>
  <svg width="0" height="0" style="position:absolute">
    <defs>
      <linearGradient id="title-fill" x1="0" y1="0" x2="1" y2="0">
        <stop offset="0" stop-color="#2a1aa8"/>
        <stop offset=".6" stop-color="#3a20c8"/>
        <stop offset="1" stop-color="#1fa0e8"/>
      </linearGradient>
    </defs>
  </svg>

  <section class="ad ad--poster">
    <div class="glove-photo" role="img" aria-label="Close-up photo of hands in blue nitrile exam gloves"></div>
    <div class="brand-tag">KelpTorch.com</div>
    <div class="promo-stamp">
      <span class="stamp-band stamp-kicker">SPECIAL <span class="light">OFFER</span></span>
      <span class="stamp-band stamp-title">CYBER MONDAY</span>
      <span class="stamp-band stamp-sale">SALE</span>
    </div>
    <svg class="product-title" viewBox="0 0 410 150">
      <text x="205" y="66" text-anchor="middle" font-size="86" stroke-width="8" textLength="300" lengthAdjust="spacingAndGlyphs">NITRILE</text>
      <text x="205" y="140" text-anchor="middle" font-size="88" stroke-width="8" textLength="318" lengthAdjust="spacingAndGlyphs">GLOVES</text>
    </svg>
    <p class="offer-copy">We are offering a box of 100,<br>no powder exam grade nitrile<br>gloves for $9.99</p>
    <p class="sale-deadline">SALES ENDS ON 4TH DECEMBER, 2021</p>
    <div class="case-price">
      <span class="case-label">Each<span class="sm">Case is</span></span>
      <span class="case-amount">$99</span>
    </div>
    <p class="site-url">www.kelptorch.com</p>
  </section>

  <section class="ad ad--banner">
    <div class="glove-photo" role="img" aria-label="Photo of hands in blue nitrile exam gloves with loose gloves at left"></div>
    <div class="brand-tag">KelpTorch.com</div>
    <div class="promo-stamp">
      <span class="stamp-band stamp-kicker">SPECIAL <span class="light">OFFER</span></span>
      <span class="stamp-band stamp-title">CYBER MONDAY</span>
      <span class="stamp-band stamp-sale">SALE</span>
    </div>
    <svg class="product-title" viewBox="0 0 519 50">
      <text x="262" y="43" text-anchor="middle" font-size="50" stroke-width="5" textLength="378" lengthAdjust="spacingAndGlyphs">NITRILE GLOVES</text>
    </svg>
    <p class="offer-copy">We are offering a box of 100,<br>no powder exam grade nitrile gloves for $9.99</p>
    <p class="sale-deadline">SALES ENDS ON 4TH DECEMBER, 2021</p>
    <div class="case-price">
      <span class="case-label">Each<span class="sm">Case is</span></span>
      <span class="case-amount">$99</span>
    </div>
    <p class="site-url">www.kelptorch.com</p>
  </section>
</body>
</html>
```